Business Card Design

We Need a business card design for my company based in Tv Radio and music Productions and hunt Talent.

Industry/Entity Type

Business

Contact Information for Business Card

BrivaTune Production's, Renzo Bettafiore,Cell Phone 427 5139048
Musician, Productor, Hunt Talent. Miami Fla. www.brivatune.net Mail. renzobettafiore@kovamail.com

```html
<!DOCTYPE html>
<html lang="en">
<head>
<meta charset="utf-8">
<title>BrivaTune Production's – Business Card</title>
<link rel="stylesheet" href="https://fonts.googleapis.com/css2?family=PT+Sans:wght@400;700&display=swap">
<style>
  :root {
    --bg: #e7e2da;
    --card: #efedea;
    --ink: #2a2a2a;
    --red: #a8322a;
    --purple: #6a3fa0;
    --yellow: #f2c230;
    --black: #111111;
    --rule: #c9c4be;
  }
  * { margin: 0; padding: 0; box-sizing: border-box; }
  html, body { width: 1200px; height: 1024px; overflow: hidden; }
  body {
    background: var(--bg);
    font-family: "PT Sans", Arial, sans-serif;
    position: relative;
  }
  .card {
    position: absolute;
    width: 580px;
    height: 330px;
    background: var(--card);
    box-shadow: 0 6px 18px rgba(0,0,0,0.18);
    overflow: hidden;
  }
  .card-front { left: 40px; top: 140px; }
  .card-back { left: 580px; top: 560px; }

  .brand-mark {
    position: absolute;
    display: flex;
    align-items: center;
    gap: 10px;
    color: var(--red);
    font-weight: 700;
  }
  .brand-mark .dot {
    border-radius: 50%;
    background: var(--yellow);
  }
  .card-front .brand-mark { left: 42px; top: 62px; font-size: 28px; }
  .card-front .brand-mark .dot { width: 34px; height: 34px; }
  .card-back .brand-mark {
    left: 50%; top: 50%;
    transform: translate(-50%, -50%);
    font-size: 44px;
  }
  .card-back .brand-mark .dot { width: 52px; height: 52px; }

  .divider {
    position: absolute;
    left: 30px; top: 162px;
    width: 330px; height: 2px;
    background: linear-gradient(to right, var(--red) 70%, var(--rule));
  }
  .divider::before {
    content: "";
    position: absolute;
    left: 0; top: 0;
    width: 2px; height: 18px;
    background: var(--red);
  }

  .location {
    position: absolute;
    left: 350px; top: 52px;
  }
  .location .city { font-size: 21px; color: var(--ink); }
  .location .roles { font-size: 13px; color: var(--purple); margin-top: 2px; }

  .contact {
    position: absolute;
    left: 46px; top: 184px;
    color: var(--ink);
  }
  .contact .company { font-size: 15px; font-weight: 700; color: var(--red); margin-bottom: 22px; }
  .contact p { font-size: 16px; line-height: 24px; }
  .contact .label { color: var(--red); }

  .edge-band {
    position: absolute;
    right: 0; top: 0;
    width: 20px; height: 100%;
  }
</style>
</head>
<body>
  <section class="card card-front">
    <div class="brand-mark"><span class="dot"></span><span>BrivaTune</span></div>

    <div class="location">
      <div class="city">Miami Fla</div>
      <div class="roles">Musician, Productor, Hunt Talent</div>
    </div>

    <div class="divider"></div>

    <div class="contact">
      <div class="company">BrivaTune Production's, Renzo Bettafiore</div>
      <p><span class="label">Cell :</span> 427 5139048</p>
      <p><span class="label">Web:</span> www.brivatune.net</p>
      <p><span class="label">Email;</span> renzobettafiore@kovamail.com</p>
    </div>

    <svg class="edge-band" viewBox="0 0 20 330" preserveAspectRatio="none" aria-hidden="true">
      <rect x="0" y="0" width="20" height="330" fill="#111111"/>
      <polygon points="0,0 20,0 20,120 0,135" fill="#a8322a"/>
      <polygon points="0,135 20,120 20,130 0,145" fill="#f2c230"/>
      <polygon points="0,145 20,130 20,142 0,157" fill="#6a3fa0"/>
    </svg>
  </section>

  <section class="card card-back">
    <div class="brand-mark"><span class="dot"></span><span>BrivaTune</span></div>
  </section>
</body>
</html>
```